PLUM TRACKER

WEBSITE AND HTML FOR A WEBSITE LOGO AND CONTENT ATTACHED HERES A COMPETITORS
https://www.lintorbay.com/

Coded - Design and coding required

1 page

```html
<!DOCTYPE html>
<html lang="en">
<head>
<meta charset="utf-8">
<title>Plum Tracker</title>
<link href="https://fonts.googleapis.com/css2?family=Poppins:wght@400;500;600;700&display=swap" rel="stylesheet">
<style>
:root{
  --teal:#3f8a8c;
  --teal-dark:#2f6f72;
  --pink:#e8a4bf;
  --pink-soft:#f3d3df;
  --ink:#1b1b1b;
  --night:#0d131d;
  --white:#ffffff;
  --grey:#f1f3f4;
}
*{box-sizing:border-box;margin:0;padding:0}
html,body{width:1200px;height:4521px;overflow:hidden}
body{position:relative;font-family:"Poppins",sans-serif;color:var(--ink);background:var(--white)}
.abs{position:absolute}
.bubble-btn{position:absolute;display:flex;align-items:center;justify-content:center;border-radius:12px;font-weight:600;font-size:19px}
.bubble-btn::after{content:"";position:absolute;right:28px;bottom:-12px;border-left:26px solid transparent;border-top:14px solid currentColor;color:inherit}
.btn-pink{background:var(--pink);color:var(--white)}
.btn-pink::after{border-top-color:var(--pink)}
.btn-teal{background:var(--teal);color:var(--white)}
.btn-teal::after{border-top-color:var(--teal)}
.btn-white{background:var(--white)}
.btn-white::after{border-top-color:var(--white)}

/* header */
.nav{left:35px;top:0;width:1130px;height:88px;background:var(--white);border-radius:0 0 44px 44px;z-index:3;box-shadow:0 4px 14px rgba(0,0,0,.12)}
.brand{position:absolute;font-weight:600;letter-spacing:-1px}
.nav .brand{left:75px;top:18px;font-size:30px;color:var(--teal)}
.nav-links{position:absolute;left:370px;top:28px;display:flex;gap:0;font-size:16px}
.nav-links span{display:inline-block}
.nav-links .active{color:var(--pink);border-bottom:2px solid var(--pink)}
.hero{left:0;top:0;width:1200px;height:688px;background:linear-gradient(110deg,#4a4036 0%,#7a6a58 40%,#b6aa9a 65%,#5b5f6a 100%)}
.hero-card{left:74px;top:237px;width:535px;height:277px;background:rgba(255,255,255,.93);border-radius:14px;padding:16px 50px}
.hero-card::after{content:"";position:absolute;right:100px;bottom:-26px;border-left:40px solid transparent;border-top:28px solid rgba(255,255,255,.93)}
.hero-card .kicker{font-size:21px}
.hero-card h1{font-size:48px;font-weight:600;letter-spacing:1px;line-height:1.1}
.hero-card p{font-size:16px;line-height:30px;margin-top:6px}

/* together */
.together{left:0;top:688px;width:1200px;height:522px;background:linear-gradient(180deg,#eef1f2,#e3e8ea 60%,#f4f6f7)}
.section-title{position:absolute;left:0;width:1200px;text-align:center;font-weight:600}
.underline{position:absolute;height:4px;background:var(--teal)}
.feature{position:absolute;width:320px;height:237px;background:var(--white);border-radius:12px;box-shadow:0 6px 16px rgba(0,0,0,.15);text-align:center;padding:38px 20px 0}
.feature h3{font-size:21px;font-weight:600;margin-bottom:10px}
.feature p{font-size:14.5px;line-height:26px}
.feature .ring{position:absolute;left:108px;top:-70px;width:104px;height:104px;border-radius:50%;border:3px solid var(--teal);background:var(--white)}
.feature .ring.pink{border-color:var(--pink)}
.feature .go{position:absolute;right:40px;bottom:-22px;width:50px;height:50px;border-radius:50%;color:var(--white);font-size:26px;display:flex;align-items:center;justify-content:center;box-shadow:0 3px 8px rgba(0,0,0,.2)}

/* about */
.about-title{left:112px;top:1262px;font-size:32px;font-weight:600;color:var(--teal)}
.about-text{left:112px;top:1340px;width:460px;font-size:14.5px;line-height:26px}
.about-photo{left:633px;top:1303px;width:432px;height:369px;border-radius:12px;background:linear-gradient(135deg,#1e1a17,#4a3a2c 55%,#2b2622)}
.about-tail{left:950px;top:1670px}

/* faq */
.faq{left:0;top:1731px;width:1200px;height:704px;background:linear-gradient(180deg,#4f9a9c,#3a8688 60%,#347c7f)}
.faq-item{position:absolute;left:228px;width:744px;background:var(--white);padding:22px 100px 0 26px;font-size:20px;font-weight:600;line-height:26px}
.faq-item .num{position:absolute;left:26px;color:var(--pink)}
.faq-item .q{margin-left:34px}
.faq-item .a{margin-left:34px;margin-top:10px;font-size:14.5px;font-weight:400;line-height:26px}
.faq-item .toggle{position:absolute;right:20px;top:30px;width:32px;height:32px;border-radius:50%;background:var(--pink);color:var(--white);font-size:22px;display:flex;align-items:center;justify-content:center;font-weight:400}

/* services */
.svc-text{position:absolute;color:var(--white)}
.svc-text h3{font-size:32px;font-weight:600;margin-bottom:8px}
.svc-text p{font-size:14.5px;line-height:26px;margin-bottom:20px}

/* contact */
.contact-band{left:0;top:3417px;width:1200px;height:421px;background:linear-gradient(180deg,#0b1220,#142236 60%,#0d1624)}
.contact-card{left:110px;top:3601px;width:978px;height:512px;background:var(--white);border-radius:14px;box-shadow:0 6px 18px rgba(0,0,0,.18)}
.field{position:absolute;width:275px;height:49px;background:var(--pink-soft);font-size:15px;padding:14px 16px}
.contact-line{position:absolute;left:163px;font-size:15px;display:flex;align-items:center;gap:10px}

/* footer */
.footer{left:0;top:4155px;width:1200px;height:366px;background:#000}
.footer-nav{position:absolute;top:4292px;left:0;width:1200px;color:var(--white);font-size:16px;font-weight:500}
.footer-nav span{position:absolute}
.social{position:absolute;top:4354px;width:25px;height:25px;border-radius:50%;background:var(--white)}
</style>
</head>
<body>

<!-- header -->
<section class="abs hero" role="img" aria-label="Photo of a man at a laptop in a video call with creators"></section>
<header class="abs nav">
  <div class="brand">PLUM TRACKER</div>
  <nav class="nav-links">
    <span class="active" style="margin-left:0">Home</span>
    <span style="margin-left:45px">Together</span>
    <span style="margin-left:45px">Services</span>
    <span style="margin-left:45px">About</span>
    <span style="margin-left:45px">FAQ</span>
  </nav>
  <div class="bubble-btn btn-pink" style="left:840px;top:9px;width:215px;height:55px">Free Consultation</div>
</header>
<div class="abs hero-card">
  <div class="kicker">Welcome To</div>
  <h1>PLUM TRACKER</h1>
  <p>Plum Tracker is a full-service FanVault management agency that specialises in chat management, promotion and traffic analysis.</p>
  <div class="bubble-btn btn-pink" style="left:52px;top:209px;width:155px;height:50px">Get Started</div>
</div>

<!-- together -->
<section class="abs together" role="img" aria-label="Faint background photo of an office"></section>
<h2 class="section-title" style="top:728px;font-size:31px;color:var(--teal)">Stronger. Together.</h2>
<div class="underline" style="left:538px;top:784px;width:124px"></div>

<div class="feature" style="left:82px;top:824px">
  <div class="ring"></div>
  <h3>Power to creators.</h3>
  <p>We take care of your FanVault account, so you can focus on creating content for your fans. Plum Tracker makes your experience as a content creator simple and stress free.</p>
  <div class="go" style="background:var(--teal)">&gt;</div>
</div>
<div class="feature" style="left:444px;top:910px">
  <div class="ring pink"></div>
  <h3>Building together.</h3>
  <p>Connecting to our creators on a personal level is essential to us. We need to know you in order to understand what is best for you. We work together as a team.</p>
  <div class="go" style="background:var(--pink)">&gt;</div>
</div>
<div class="feature" style="left:802px;top:824px">
  <div class="ring"></div>
  <h3>Personalised growth.</h3>
  <p>Every creator is unique and requires a distinct approach. Using powerful analytic tools we are able to optimise your social media outlets and reach millions of potential clients.</p>
  <div class="go" style="background:var(--teal)">&gt;</div>
</div>

<!-- about -->
<h2 class="abs about-title">About Us</h2>
<div class="abs about-text">
  <p>I have multiple years of experience in high-end video (post)production and cross-media content creation with clients ranging from Brewline to Halden &amp; Co. Because of my technical knowledge and experience in the film industry,</p>
  <p style="margin-top:50px">I can guide you in the process of making high quality video and photo. I will provide you with tips and tricks to give your images a professional look and elevate your content to a higher level.</p>
</div>
<div class="bubble-btn btn-teal" style="left:110px;top:1628px;width:155px;height:51px">Learn More</div>
<div class="abs about-photo" role="img" aria-label="Photo of a woman working at a desk in a dark room"></div>
<svg class="abs about-tail" width="60" height="24"><polygon points="0,0 52,0 55,22" fill="#2b2622"/></svg>

<!-- faq -->
<section class="abs faq" role="img" aria-label="Teal tinted background photo of a city"></section>
<h2 class="section-title" style="top:1774px;font-size:31px;color:var(--white)">Frequent Asked Questions</h2>
<div class="underline" style="left:538px;top:1826px;width:124px;background:var(--white)"></div>

<div class="faq-item" style="top:1854px;height:140px">
  <span class="num">1.</span>
  <div class="q">What do your services include?</div>
  <div class="a">Chat management, copywriting, content scheduling, viral social media strategies, content plans and more! Our services are tailored specifically for you.</div>
  <div class="toggle">&minus;</div>
</div>
<div class="faq-item" style="top:2019px;height:100px">
  <span class="num">2.</span>
  <div class="q">I don’t have an FanVault account or I have a very small subscriber base, is this service right for me?</div>
  <div class="toggle">+</div>
</div>
<div class="faq-item" style="top:2142px;height:100px">
  <span class="num">3.</span>
  <div class="q">When can I get started?</div>
  <div class="toggle">+</div>
</div>
<div class="faq-item" style="top:2266px;height:100px">
  <span class="num">4.</span>
  <div class="q">I already have a large following, but I cannot manage it on my own anymore, is this service right for me?</div>
  <div class="toggle">+</div>
</div>

<!-- services -->
<h2 class="section-title" style="top:2480px;font-size:31px">Services</h2>
<div class="underline" style="left:566px;top:2529px;width:68px;background:var(--ink)"></div>

<div class="abs" style="left:0;top:2575px;width:591px;height:384px;background:var(--pink)"></div>
<div class="abs" style="left:591px;top:2575px;width:609px;height:384px;background:linear-gradient(135deg,#1c3a5a,#3d6e94 50%,#7fa6c2)" role="img" aria-label="Photo of hands typing on a laptop with dollar symbols"></div>
<div class="svc-text" style="left:110px;top:2615px;width:410px">
  <h3>Earning</h3>
  <p>Our trained team manages your chat 7 days a week to retain and gain more subscribers. The constant stream of messages can become hard to keep up with for creators.</p>
  <p>We take care of your chats and have shown to increase income from messages by up to a 100 times.</p>
</div>
<div class="bubble-btn btn-white" style="left:111px;top:2867px;width:154px;height:50px;color:var(--pink)">Learn More</div>

<div class="abs" style="left:0;top:2959px;width:591px;height:382px;background:linear-gradient(135deg,#0f2a40,#2f5878 55%,#1a3550)" role="img" aria-label="Photo of a hand touching a marketing strategy graphic"></div>
<div class="abs" style="left:591px;top:2959px;width:609px;height:382px;background:var(--teal)"></div>
<div class="svc-text" style="left:709px;top:2998px;width:370px">
  <h3>Viral strategies</h3>
  <p>We offer a personalised growth plan to every creator in order to maximise your reach. Our strategies have made creators go viral and amass millions of views on ClipStream.</p>
  <p>Our creators have gained thousands of paid fans from viral ClipStream video’s.</p>
</div>
<div class="bubble-btn btn-white" style="left:709px;top:3250px;width:155px;height:50px;color:var(--teal)">Learn More</div>

<!-- contact -->
<section class="abs contact-band" role="img" aria-label="Dark background photo of a workspace"></section>
<h2 class="section-title" style="top:3478px;font-size:31px;color:var(--white)">Contact Us</h2>
<div class="underline" style="left:566px;top:3526px;width:68px;background:var(--white)"></div>
<p class="section-title" style="top:3553px;font-size:14.5px;font-weight:500;color:var(--white)">Lorem Ipsum is simply dummy text of the printing and typesetting industry.</p>

<div class="abs contact-card"></div>
<h3 class="abs" style="left:161px;top:3660px;font-size:31px;font-weight:600">Get In Touch</h3>
<p class="abs" style="left:161px;top:3715px;width:250px;font-size:14.5px;line-height:26px">Want to become a top earner or need help managing a large subscriber base?</p>
<h4 class="abs" style="left:169px;top:3836px;font-size:21px;font-weight:600">Contact Us</h4>
<div class="contact-line" style="top:3877px">
  <svg width="14" height="14" viewBox="0 0 24 24"><path d="M6.6 10.8a15 15 0 0 0 6.6 6.6l2.2-2.2a1 1 0 0 1 1-.25 11.4 11.4 0 0 0 3.6.6 1 1 0 0 1 1 1V20a1 1 0 0 1-1 1A17 17 0 0 1 3 4a1 1 0 0 1 1-1h3.5a1 1 0 0 1 1 1c0 1.25.2 2.45.6 3.6a1 1 0 0 1-.25 1z" fill="#1b1b1b"/></svg>
  +1 5550 123 4567</div>
<div class="contact-line" style="top:3920px">
  <svg width="14" height="12" viewBox="0 0 24 20"><rect x="1" y="2" width="22" height="16" fill="#1b1b1b"/><polyline points="1,3 12,11 23,3" fill="none" stroke="#fff" stroke-width="2"/></svg>
  info@plumtracker.com</div>
<div class="contact-line" style="top:3960px">
  <svg width="14" height="18" viewBox="0 0 24 32"><path d="M12 0a10 10 0 0 0-10 10c0 8 10 22 10 22s10-14 10-22A10 10 0 0 0 12 0zm0 14a4 4 0 1 1 0-8 4 4 0 0 1 0 8z" fill="#1b1b1b"/></svg>
  Plum Tracker, United States</div>

<div class="field" style="left:430px;top:3652px">Name</div>
<div class="field" style="left:756px;top:3652px">Email</div>
<div class="field" style="left:430px;top:3729px">ClipStream</div>
<div class="field" style="left:756px;top:3729px">Your FanVault URL</div>
<div class="field" style="left:430px;top:3806px">ChatLine</div>
<div class="field" style="left:756px;top:3806px">Relay</div>
<div class="field" style="left:430px;top:3880px;width:605px;height:97px">Message</div>
<div class="abs" style="left:430px;top:4005px;width:176px;height:53px;background:var(--teal);color:var(--white);font-size:19px;font-weight:600;display:flex;align-items:center;justify-content:center">Submit Request</div>

<!-- footer -->
<footer class="abs footer"></footer>
<div class="brand" style="left:0;width:1200px;text-align:center;top:4220px;font-size:36px;color:var(--teal)">PLUM TRACKER</div>
<div class="footer-nav">
  <span style="left:320px">Home</span>
  <span style="left:440px">Together</span>
  <span style="left:585px">Services</span>
  <span style="left:725px">About</span>
  <span style="left:845px">FAQ</span>
</div>
<div class="social" style="left:531px"></div>
<div class="social" style="left:569px"></div>
<div class="social" style="left:606px"></div>
<div class="social" style="left:643px"></div>
<div class="abs" style="left:110px;top:4434px;width:980px;height:1px;background:#555"></div>
<p class="abs" style="left:0;width:1200px;text-align:center;top:4464px;font-size:15px;font-weight:500;color:var(--white)">Copy Rights@2022.<span style="color:var(--pink)">Plum</span> <span style="color:var(--teal)">Tracker</span>.All Rights Reserved</p>

</body>
</html>
```